IT Services company

we want a modern card design that combines business and technology whilst not being too loud

the Company Name is Corvane Hub and i have attached the logo

can you also put the words Technology Built For Business under the logo

thanks

Hi can you please show the card with a web url and contact name and email and phone number please

Business

```html
<!DOCTYPE html>
<html lang="en">
<head>
<meta charset="utf-8">
<title>Corvane Hub – Business Cards</title>
<link rel="stylesheet" href="https://fonts.googleapis.com/css2?family=Arimo:wght@400;700&display=swap">
<style>
  :root {
    --backdrop: #dcdcdc;
    --card: #f6f6f6;
    --brand-red: #a8372a;
    --brand-red-light: #d04a36;
    --brand-blue: #4a62b0;
    --ink: #2b2b2b;
    --ink-soft: #5a5a5a;
    --rule: #c9c9c9;
  }
  * { box-sizing: border-box; margin: 0; padding: 0; }
  html, body { width: 1200px; height: 777px; overflow: hidden; }
  body {
    background: var(--backdrop);
    font-family: "Arimo", Arial, sans-serif;
    color: var(--ink);
    position: relative;
  }
  .card {
    position: absolute;
    width: 520px;
    height: 298px;
    background: var(--card);
    border-radius: 24px;
    overflow: hidden;
    box-shadow: 0 6px 18px rgba(0,0,0,.18);
  }
  .card--front { left: 60px; top: 240px; }
  .card--back  { left: 620px; top: 240px; }

  /* Brand lockup */
  .brand { position: absolute; display: flex; align-items: center; gap: 12px; white-space: nowrap; }
  .brand__dot { width: 46px; height: 46px; border-radius: 50%; background: var(--brand-red-light); flex: none; }
  .brand__name { font-weight: 700; color: var(--brand-red); font-size: 28px; letter-spacing: 2px; text-transform: uppercase; line-height: 1; }
  .tagline { font-size: 11px; color: var(--ink-soft); letter-spacing: .5px; text-transform: uppercase; margin-top: 4px; }
  .card--front .brand { right: 30px; top: 30px; }

  /* Contact person */
  .person { position: absolute; left: 30px; top: 118px; }
  .person__name { font-weight: 700; font-size: 15px; letter-spacing: 1px; text-transform: uppercase; }
  .person__role { font-size: 12.5px; color: var(--ink-soft); margin-top: 3px; }

  /* Contact row */
  .contacts { position: absolute; left: 30px; right: 30px; bottom: 40px; display: flex; align-items: flex-end; white-space: nowrap; }
  .contacts__group { font-size: 12px; line-height: 1.65; color: var(--ink-soft); padding-right: 22px; margin-right: 22px; border-right: 1px solid var(--rule); }
  .contacts__group:last-child { border-right: none; margin-right: 0; padding-right: 0; }
  .contacts__item { display: flex; align-items: center; gap: 7px; }
  .icon { width: 12px; height: 12px; flex: none; }

  /* Colour bands */
  .band { position: absolute; bottom: 0; }
  .band--blue { left: 0; width: 190px; height: 9px; background: var(--brand-blue); }
  .band--red { left: 194px; right: 0; height: 14px; background: var(--brand-red); }

  /* Back */
  .back__disc {
    position: absolute; left: -60px; top: 110px; width: 240px; height: 240px; border-radius: 50%;
    background: radial-gradient(circle at 40% 35%, var(--brand-red-light), var(--brand-red));
  }
  .card--back .brand { left: 200px; top: 100px; display: block; }
  .card--back .brand__name { font-size: 32px; letter-spacing: 2px; }
  .card--back .tagline { font-size: 13px; margin-top: 7px; }
</style>
</head>
<body>
  <section class="card card--front" aria-label="Business card front">
    <div class="brand">
      <span class="brand__dot"></span>
      <div>
        <div class="brand__name">Corvane Hub</div>
        <div class="tagline">Technology Built For Business</div>
      </div>
    </div>

    <div class="person">
      <div class="person__name">Dale Morrow</div>
      <div class="person__role">General Manager</div>
    </div>

    <div class="contacts">
      <div class="contacts__group">
        <div>4180 W. Alder Street</div>
        <div>Suite 200, Mesa</div>
      </div>
      <div class="contacts__group">
        <div class="contacts__item">
          <svg class="icon" viewBox="0 0 12 12"><circle cx="6" cy="6" r="6" fill="#a8372a"/><rect x="3" y="4" width="6" height="4" fill="none" stroke="#fff" stroke-width=".9"/><path d="M3 4l3 2.3L9 4" fill="none" stroke="#fff" stroke-width=".9"/></svg>
          info@corvanehub.com
        </div>
        <div class="contacts__item">
          <svg class="icon" viewBox="0 0 12 12"><circle cx="6" cy="6" r="6" fill="#a8372a"/><circle cx="6" cy="6" r="3.3" fill="none" stroke="#fff" stroke-width=".8"/><path d="M2.7 6h6.6M6 2.7c-1.6 2-1.6 4.6 0 6.6M6 2.7c1.6 2 1.6 4.6 0 6.6" fill="none" stroke="#fff" stroke-width=".7"/></svg>
          www.corvanehub.com
        </div>
      </div>
      <div class="contacts__group">
        <div class="contacts__item">
          <svg class="icon" viewBox="0 0 12 12"><circle cx="6" cy="6" r="6" fill="#a8372a"/><path d="M4 3.2l1.2 1.3-.7.9c.4.9 1.2 1.7 2.1 2.1l.9-.7 1.3 1.2-.8.9C6 8.8 3.2 6 3.1 4z" fill="#fff"/></svg>
          (555) 214-3080
        </div>
        <div class="contacts__item">
          <svg class="icon" viewBox="0 0 12 12"><circle cx="6" cy="6" r="6" fill="#a8372a"/><rect x="3" y="3.5" width="6" height="5" rx=".6" fill="#fff"/></svg>
          (555) 214-3091
        </div>
      </div>
    </div>

    <div class="band band--blue"></div>
    <div class="band band--red"></div>
  </section>

  <section class="card card--back" aria-label="Business card back">
    <div class="back__disc"></div>
    <div class="brand">
      <div class="brand__name">Corvane Hub</div>
      <div class="tagline">Technology Built For Business</div>
    </div>
  </section>
</body>
</html>
```